I need a simple infographic that describes the 4 basic elements of how to effectively create change.

The overall title (Gentle Pressure Relentlessly Applied) should be at the top of the infographic. Subtitle is: "Leading Change".
There are four steps:
1. Alignment- Agreement on Approach
2. Transparency- Metrics for Assurance
3. Skills- Training and Coaching
4. Integrity- Culture of Accountability

Target Market(s)

Business Leaders in a training workshop

Font styles to use
Serif

Requirements
Must have
• Here are the 4 elements of the Infographic: Please show them in order.
• 1. Agreement on Approach. (Alignment)
• 2. Metrics for Assurance (Transparency)
• 3. Training and Coaching (Skills)
• 4. Culture of Accountability (Integrity)
Nice to have
• Cool Graphics that depict the 4 steps.
Should not have
• Pictures.

```html
<!DOCTYPE html>
<html lang="en">
<head>
<meta charset="utf-8">
<title>Gentle Pressure Relentlessly Applied – Leading Change</title>
<link rel="stylesheet" href="https://fonts.googleapis.com/css2?family=Montserrat:wght@400;500;600;700&family=Raleway:wght@700;800&display=swap">
<style>
  :root{
    --page:#e9edf0;
    --teal:#1fb9d2;
    --teal-light:#3ccbe0;
    --teal-deep:#0e7c89;
    --navy:#242935;
    --ink-dark:#2d3038;
  }
  html,body{margin:0;padding:0;overflow:hidden}
  body{width:1038px;height:1200px;background:var(--page);font-family:"Montserrat",sans-serif}
  .sheet{display:flex;flex-direction:column;align-items:center;gap:40px;padding-top:19px}
  .panel{display:block;width:1000px;height:560px}
  .panel--dark{--bg:var(--navy);--ink:#ffffff;--subtitle:#ffffff}
  .panel--light{--bg:#ffffff;--ink:var(--ink-dark);--subtitle:var(--teal)}
  .panel__bg{fill:var(--bg)}
  text{text-anchor:middle}
  .brand{font-family:"Montserrat",sans-serif;font-weight:500;font-size:24px;fill:var(--ink);text-anchor:start}
  .brand-dot{fill:none;stroke:var(--ink);stroke-width:2.5}
  .banner__band{fill:url(#bandFill)}
  .banner__tail{fill:var(--teal-deep)}
  .banner__fold{fill:#0a5f6a}
  .banner__title{font-family:"Raleway",sans-serif;font-weight:800;font-size:25px;fill:#fff;letter-spacing:.2px}
  .subtitle{font-size:24px;fill:var(--subtitle)}
  .step__num-ring{fill:none;stroke:var(--teal);stroke-width:2}
  .step__num{font-size:16px;font-weight:500;fill:var(--teal)}
  .ring-solid{fill:none;stroke:var(--teal);stroke-width:2.5}
  .ring-dash{fill:none;stroke:var(--teal);stroke-width:2;stroke-dasharray:5 4}
  .ring-inner{fill:none;stroke:var(--teal);stroke-width:3}
  .ring-arrow{fill:none;stroke:var(--teal);stroke-width:2.5;stroke-linejoin:round}
  .ring-start{fill:var(--bg);stroke:var(--teal);stroke-width:2.5}
  .icon-line{fill:none;stroke:var(--teal);stroke-width:3;stroke-linecap:round;stroke-linejoin:round}
  .icon-bar{stroke:var(--teal);stroke-width:7;stroke-linecap:round}
  .step__pill{fill:var(--teal)}
  .step__label{font-size:17px;font-weight:600;fill:#fff}
  .step__desc{font-size:16px;fill:var(--ink)}
</style>
</head>
<body>
<svg width="0" height="0" style="position:absolute" aria-hidden="true">
  <defs>
    <linearGradient id="bandFill" x1="0" x2="1" y1="0" y2="0">
      <stop offset="0" stop-color="#37c6dc"/>
      <stop offset="1" stop-color="#17afc8"/>
    </linearGradient>
    <symbol id="ring-a" viewBox="-120 -120 240 240" overflow="visible">
      <path class="ring-dash" d="M-100 0 A100 100 0 0 1 100 0"/>
      <path class="ring-solid" d="M100 0 A100 100 0 0 1 -100 0"/>
      <circle class="ring-inner" r="86"/>
      <path class="ring-arrow" d="M92 12 L100 0 L108 12"/>
    </symbol>
    <symbol id="ring-b" viewBox="-120 -120 240 240" overflow="visible">
      <path class="ring-solid" d="M-100 0 A100 100 0 0 1 100 0"/>
      <path class="ring-dash" d="M100 0 A100 100 0 0 1 -100 0"/>
      <circle class="ring-inner" r="86"/>
      <path class="ring-arrow" d="M92 -6 L100 6 L108 -6"/>
    </symbol>
    <symbol id="icon-align" viewBox="-40 -40 80 80" overflow="visible">
      <line class="icon-bar" x1="-32" y1="-24" x2="32" y2="-24"/>
      <line class="icon-bar" x1="-22" y1="-8" x2="22" y2="-8"/>
      <line class="icon-bar" x1="-32" y1="8" x2="32" y2="8"/>
      <line class="icon-bar" x1="-22" y1="24" x2="22" y2="24"/>
    </symbol>
    <symbol id="icon-metrics" viewBox="-40 -40 80 80" overflow="visible">
      <rect class="icon-line" x="-14" y="-34" width="44" height="56" rx="3"/>
      <line class="icon-line" x1="14" y1="-22" x2="24" y2="-22"/>
      <line class="icon-line" x1="18" y1="-12" x2="24" y2="-12"/>
      <line class="icon-line" x1="18" y1="-2" x2="24" y2="-2"/>
      <line class="icon-line" x1="-8" y1="12" x2="24" y2="12"/>
      <circle class="icon-line" cx="-10" cy="-10" r="20" style="fill:var(--bg)"/>
      <path class="icon-line" d="M-22 -10 Q-10 -22 2 -10 Q-10 2 -22 -10Z"/>
      <circle cx="-10" cy="-10" r="4" style="fill:var(--teal)"/>
      <line class="icon-line" x1="4" y1="4" x2="26" y2="30" style="stroke-width:6"/>
    </symbol>
    <symbol id="icon-skills" viewBox="-40 -40 80 80" overflow="visible">
      <path class="icon-line" d="M-14 10 C-26 0 -26 -32 0 -34 C26 -32 26 0 14 10 L14 18 L-14 18Z"/>
      <circle class="icon-line" cx="0" cy="-12" r="10"/>
      <path class="icon-line" d="M-6 -4 L-6 18 M6 -4 L6 18"/>
      <path class="icon-line" d="M-8 18 L-8 26 L-18 32 M8 18 L8 26 L18 32 M0 18 L0 34"/>
      <circle class="icon-line" cx="-20" cy="33" r="2.5"/>
      <circle class="icon-line" cx="20" cy="33" r="2.5"/>
    </symbol>
    <symbol id="icon-integrity" viewBox="-40 -40 80 80" overflow="visible">
      <circle class="icon-line" cx="-6" cy="-18" r="13"/>
      <path class="icon-line" d="M-32 30 L-32 16 C-32 4 -22 -2 -6 -2 C2 -2 8 0 12 2 M8 30 L-32 30"/>
      <path class="icon-line" d="M20 -2 L34 4 L34 14 C34 24 26 30 20 32 C14 30 6 24 6 14 L6 4Z" style="fill:var(--bg)"/>
      <path class="icon-line" d="M13 14 L18 19 L27 9"/>
    </symbol>
  </defs>
</svg>

<main class="sheet">
  <svg class="panel panel--dark" viewBox="0 0 1000 560" role="group" aria-label="Leading Change infographic, dark version">
    <rect class="panel__bg" width="1000" height="560"/>
    <g class="brand-lockup">
      <circle class="brand-dot" cx="404" cy="45" r="12"/>
      <text class="brand" x="426" y="54">Halden Partners</text>
    </g>
    <g class="banner">
      <path class="banner__tail" d="M180 92 L238 92 L238 140 L180 140 L198 116Z"/>
      <path class="banner__tail" d="M820 92 L762 92 L762 140 L820 140 L802 116Z"/>
      <path class="banner__fold" d="M210 128 L238 140 L238 128Z M790 128 L762 140 L762 128Z"/>
      <rect class="banner__band" x="210" y="78" width="580" height="50"/>
      <text class="banner__title" x="500" y="112">GENTLE PRESSURE RELENTLESSLY APPLIED</text>
    </g>
    <text class="subtitle" x="500" y="166">"Leading Change"</text>

    <g class="step" transform="translate(209 0)">
      <circle class="step__num-ring" cy="205" r="17"/><text class="step__num" y="211">1</text>
      <use href="#ring-a" x="-120" y="215" width="240" height="240"/>
      <circle class="ring-start" cx="-100" cy="335" r="7"/>
      <use href="#icon-align" x="-50" y="285" width="100" height="100"/>
      <rect class="step__pill" x="-70" y="446" width="140" height="30" rx="15"/>
      <text class="step__label" y="467">Alignment</text>
      <text class="step__desc" y="501">Agreement</text><text class="step__desc" y="521">on Approach</text>
    </g>
    <g class="step" transform="translate(403 0)">
      <circle class="step__num-ring" cy="205" r="17"/><text class="step__num" y="211">2</text>
      <use href="#ring-b" x="-120" y="215" width="240" height="240"/>
      <use href="#icon-metrics" x="-50" y="285" width="100" height="100"/>
      <rect class="step__pill" x="-70" y="446" width="140" height="30" rx="15"/>
      <text class="step__label" y="467">Transparency</text>
      <text class="step__desc" y="501">Metrics</text><text class="step__desc" y="521">for Assurance</text>
    </g>
    <g class="step" transform="translate(595 0)">
      <circle class="step__num-ring" cy="205" r="17"/><text class="step__num" y="211">3</text>
      <use href="#ring-a" x="-120" y="215" width="240" height="240"/>
      <use href="#icon-skills" x="-50" y="285" width="100" height="100"/>
      <rect class="step__pill" x="-70" y="446" width="140" height="30" rx="15"/>
      <text class="step__label" y="467">Skills</text>
      <text class="step__desc" y="501">Training</text><text class="step__desc" y="521">and Coaching</text>
    </g>
    <g class="step" transform="translate(791 0)">
      <circle class="step__num-ring" cy="205" r="17"/><text class="step__num" y="211">4</text>
      <use href="#ring-b" x="-120" y="215" width="240" height="240"/>
      <use href="#icon-integrity" x="-50" y="285" width="100" height="100"/>
      <rect class="step__pill" x="-70" y="446" width="140" height="30" rx="15"/>
      <text class="step__label" y="467">Integrity</text>
      <text class="step__desc" y="501">Culture</text><text class="step__desc" y="521">of Accountability</text>
    </g>
  </svg>

  <svg class="panel panel--light" viewBox="0 0 1000 560" role="group" aria-label="Leading Change infographic, light version">
    <rect class="panel__bg" width="1000" height="560"/>
    <g class="brand-lockup">
      <circle class="brand-dot" cx="404" cy="45" r="12"/>
      <text class="brand" x="426" y="54">Halden Partners</text>
    </g>
    <g class="banner">
      <path class="banner__tail" d="M180 92 L238 92 L238 140 L180 140 L198 116Z"/>
      <path class="banner__tail" d="M820 92 L762 92 L762 140 L820 140 L802 116Z"/>
      <path class="banner__fold" d="M210 128 L238 140 L238 128Z M790 128 L762 140 L762 128Z"/>
      <rect class="banner__band" x="210" y="78" width="580" height="50"/>
      <text class="banner__title" x="500" y="112">GENTLE PRESSURE RELENTLESSLY APPLIED</text>
    </g>
    <text class="subtitle" x="500" y="166">"Leading Change"</text>

    <g class="step" transform="translate(209 0)">
      <circle class="step__num-ring" cy="205" r="17"/><text class="step__num" y="211">1</text>
      <use href="#ring-a" x="-120" y="215" width="240" height="240"/>
      <circle class="ring-start" cx="-100" cy="335" r="7"/>
      <use href="#icon-align" x="-50" y="285" width="100" height="100"/>
      <rect class="step__pill" x="-70" y="446" width="140" height="30" rx="15"/>
      <text class="step__label" y="467">Alignment</text>
      <text class="step__desc" y="501">Agreement</text><text class="step__desc" y="521">on Approach</text>
    </g>
    <g class="step" transform="translate(403 0)">
      <circle class="step__num-ring" cy="205" r="17"/><text class="step__num" y="211">2</text>
      <use href="#ring-b" x="-120" y="215" width="240" height="240"/>
      <use href="#icon-metrics" x="-50" y="285" width="100" height="100"/>
      <rect class="step__pill" x="-70" y="446" width="140" height="30" rx="15"/>
      <text class="step__label" y="467">Transparency</text>
      <text class="step__desc" y="501">Metrics</text><text class="step__desc" y="521">for Assurance</text>
    </g>
    <g class="step" transform="translate(595 0)">
      <circle class="step__num-ring" cy="205" r="17"/><text class="step__num" y="211">3</text>
      <use href="#ring-a" x="-120" y="215" width="240" height="240"/>
      <use href="#icon-skills" x="-50" y="285" width="100" height="100"/>
      <rect class="step__pill" x="-70" y="446" width="140" height="30" rx="15"/>
      <text class="step__label" y="467">Skills</text>
      <text class="step__desc" y="501">Training</text><text class="step__desc" y="521">and Coaching</text>
    </g>
    <g class="step" transform="translate(791 0)">
      <circle class="step__num-ring" cy="205" r="17"/><text class="step__num" y="211">4</text>
      <use href="#ring-b" x="-120" y="215" width="240" height="240"/>
      <use href="#icon-integrity" x="-50" y="285" width="100" height="100"/>
      <rect class="step__pill" x="-70" y="446" width="140" height="30" rx="15"/>
      <text class="step__label" y="467">Integrity</text>
      <text class="step__desc" y="501">Culture</text><text class="step__desc" y="521">of Accountability</text>
    </g>
  </svg>
</main>
</body>
</html>
```